Broschüre
Zielgruppe
Wir sind eine ambulanter Pflegedienst in Rostock. Ab dem Herbst 25 bieten wir für Interessenten mit einem Pflegegrad begleitete reisen an. Eine Fachkraft wird Patienten mit Pflegegrad in kleinen Gruppen begleiten. Den Text für den Flyer haben wir eingefügt. Bitte die Bider aus dem Stock Portal wählen. Über den Flyer sollen Patienten gefunden werden.
Der Flyer
sollte Serios wirken und Reiselust der Senioren wecken.
Aufgabenstellung
Hier der Text für den Flyer:
Was wir bieten:
✔️ Begleitung durch erfahrene Pflegefachkräfte ✔️ Körperpflege, Medikamentengabe & Betreuung wie zuhause ✔️ 24-Stunden-Erreichbarkeit unserer Pflegekräfte vor Ort im gebuchten Hotel ✔️ Zusammenarbeit mit ausgewählten Hotels – barrierefrei & seniorengerecht ✔️ Kleine Gruppen & individuelle Betreuung vor Ort
Gut zu wissen:
Für unsere pflegerische Begleitung entstehen Ihnen keine zusätzlichen Kosten, wenn Sie einen Pflegegrad haben und das Verhinderungspflege-Budget noch nicht aufgebraucht ist.
Lediglich die Hotelkosten sind von Ihnen selbst zu tragen.
Wer hat Anspruch auf Verhinderungspflege?
Alle Pflegebedürftigen mit einem anerkannten Pflegegrad ab Stufe 2 können jährlich Verhinderungspflege über die Pflegekasse abrufen – ideal, um sich im Urlaub sicher begleiten zu lassen!
Unser Service – Ihr Mehrwert:
Wir organisieren Ihre Reise von A bis Z und begleiten Sie oder Ihre Angehörigen auf dem Weg zu Erholung und neuen Eindrücken – mit Herz, Kompetenz und Erfahrung. Vor Ort sind müssen Sie auf nichts verzichten und werden versorgt wie zu Hause. Gerne organisieren wir auch die Abholung aus ihrer Hässlichkeit.
???? Sonnenweg Touren – Ihr verlässlicher Partner für Pflege und Lebensfreude
???? Jetzt informieren & Platz sichern: 0381 - 72946183
???? Mail@sonnenweg-touren .de
???? www.sonnenweg-touren.de

```html
<!DOCTYPE html>
<html lang="de">
<head>
<meta charset="utf-8">
<title>Reiselust trotz Pflegegrad – Flyer</title>
<link href="https://fonts.googleapis.com/css2?family=Plus+Jakarta+Sans:wght@400;500;700;800&display=swap" rel="stylesheet">
<style>
  :root{
    --stage:#efedee;
    --paper:#ffffff;
    --navy:#1f2747;
    --blue:#2a7bc4;
    --orange:#f65a2c;
    --orange-light:#ff7a4a;
    --ink:#1f2747;
    --text:#2b2f3a;
  }
  *{margin:0;padding:0;box-sizing:border-box}
  html,body{width:811px;height:1200px;overflow:hidden;background:var(--stage);
    font-family:"Plus Jakarta Sans",Arial,sans-serif;color:var(--text)}
  .canvas{position:relative;width:811px;height:1200px}
  .page{position:absolute;top:335px;width:375px;height:529px;background:var(--paper);
    box-shadow:0 6px 18px rgba(0,0,0,.12);overflow:hidden}
  .page--front{left:24px}
  .page--back{left:412px}

  .hero-photo{position:absolute;left:0;top:0;width:375px;height:378px;
    background:radial-gradient(circle at 45% 40%,#d9b9a4 0 14%,transparent 34%),
      linear-gradient(180deg,var(--orange-light) 0%,var(--orange) 55%,#1f8fb0 100%)}
  .band{position:absolute;left:0;top:0;width:375px;height:529px}
  .headline{position:absolute;left:0;width:375px;text-align:center;top:405px;
    font-weight:800;font-size:23px;letter-spacing:-.3px;color:#fff}
  .headline .accent{color:var(--blue)}
  .subline{position:absolute;left:0;width:375px;text-align:center;top:434px;
    font-size:18px;font-weight:400;color:#fff}
  .url{position:absolute;font-size:12.5px;font-weight:500;color:#111;top:493px}
  .page--front .url{right:29px}
  .page--back .url{left:33px}

  .badge{position:absolute;width:82px;height:58px;background:var(--blue);border-radius:50%;
    transform:rotate(-16deg);color:#fff;font-weight:800;text-align:center;
    display:flex;flex-direction:column;justify-content:center;line-height:1.05}
  .badge--new{left:274px;top:328px;font-size:11px}
  .badge--cta{left:278px;top:438px;font-size:8.5px;width:84px;height:62px}

  .content{position:absolute;left:33px;top:26px;width:305px}
  .content h2{font-size:10.5px;font-weight:700;color:var(--ink);margin-bottom:2px}
  .content p{font-size:8.4px;line-height:12px;margin-bottom:14px}
  .checklist{list-style:none;margin:4px 0 12px}
  .checklist li{position:relative;padding-left:14px;font-size:8.4px;line-height:10.5px;margin-bottom:5px}
  .checklist svg{position:absolute;left:0;top:1px}

  .contact{position:absolute;left:0;top:388px;width:375px;text-align:center;color:#fff}
  .contact .name{font-size:10.5px;font-weight:700}
  .contact .claim{font-size:10.5px;font-weight:700;color:var(--blue);margin-bottom:12px}
  .contact .line{font-size:10.5px;display:flex;align-items:center;justify-content:center;gap:5px;margin-bottom:6px}
</style>
</head>
<body>
<div class="canvas">

  <section class="page page--front">
    <div class="hero-photo" role="img" aria-label="Fröhlicher Senior mit Strohhut, herzförmiger Sonnenbrille und buntem Hawaiihemd hält einen Cocktail vor orangem Hintergrund"></div>
    <svg class="band" viewBox="0 0 375 529" aria-hidden="true">
      <polygon points="0,378 375,378 375,469 0,483" fill="var(--navy)"/>
    </svg>
    <div class="badge badge--new"><span>Neu</span><span>ab Herbst</span><span>2025</span></div>
    <h1 class="headline">Reiselust <span class="accent">trotz Pflegegrad</span></h1>
    <p class="subline">wir machen es möglich.</p>
    <p class="url">www.sonnenweg-touren.de</p>
  </section>

  <section class="page page--back">
    <div class="content">
      <h2>Was wir bieten</h2>
      <ul class="checklist">
        <li><svg width="9" height="8" viewBox="0 0 9 8"><path d="M1 4.2 3.4 6.5 8 1" fill="none" stroke="var(--blue)" stroke-width="1.8"/></svg>Begleitung durch erfahrene Pflegefachkräfte</li>
        <li><svg width="9" height="8" viewBox="0 0 9 8"><path d="M1 4.2 3.4 6.5 8 1" fill="none" stroke="var(--blue)" stroke-width="1.8"/></svg>Körperpflege, Medikamentengabe &amp; Betreuung wie zuhause</li>
        <li><svg width="9" height="8" viewBox="0 0 9 8"><path d="M1 4.2 3.4 6.5 8 1" fill="none" stroke="var(--blue)" stroke-width="1.8"/></svg>24-Stunden-Erreichbarkeit unserer Pflegekräfte vor Ort im gebuchten Hotel</li>
        <li><svg width="9" height="8" viewBox="0 0 9 8"><path d="M1 4.2 3.4 6.5 8 1" fill="none" stroke="var(--blue)" stroke-width="1.8"/></svg>Zusammenarbeit mit ausgewählten Hotels – barrierefrei &amp; seniorengerecht</li>
        <li><svg width="9" height="8" viewBox="0 0 9 8"><path d="M1 4.2 3.4 6.5 8 1" fill="none" stroke="var(--blue)" stroke-width="1.8"/></svg>Kleine Gruppen &amp; individuelle Betreuung vor Ort</li>
      </ul>
      <h2>Gut zu wissen</h2>
      <p>Für unsere pflegerische Begleitung entstehen Ihnen keine zusätzlichen Kosten, wenn Sie einen Pflegegrad haben und das Verhinderungspflege-Budget noch nicht aufgebraucht ist. Lediglich die Hotelkosten sind von Ihnen selbst zu tragen.</p>
      <h2>Wer hat Anspruch auf Verhinderungspflege?</h2>
      <p>Alle Pflegebedürftigen mit einem anerkannten Pflegegrad ab Stufe 2 können jährlich Verhinderungspflege über die Pflegekasse abrufen – ideal, um sich im Urlaub sicher begleiten zu lassen!</p>
      <h2>Unser Service – Ihr Mehrwert</h2>
      <p>Wir organisieren Ihre Reise von A bis Z und begleiten Sie oder Ihre Angehörigen auf dem Weg zu Erholung und neuen Eindrücken – mit Herz, Kompetenz und Erfahrung. Vor Ort sind müssen Sie auf nichts verzichten und werden versorgt wie zu Hause. Gerne organisieren wir auch die Abholung aus Ihrer Häuslichkeit.</p>
    </div>
    <svg class="band" viewBox="0 0 375 529" aria-hidden="true">
      <polygon points="0,378 375,378 375,483 0,470" fill="var(--navy)"/>
    </svg>
    <div class="contact">
      <p class="name">Sonnenweg Touren –</p>
      <p class="claim">Ihr verlässlicher Partner für Pflege und Lebensfreude</p>
      <p class="line"><svg width="8" height="8" viewBox="0 0 24 24"><path d="M6.6 10.8a15.1 15.1 0 0 0 6.6 6.6l2.2-2.2a1 1 0 0 1 1-.25 11.4 11.4 0 0 0 3.6.6 1 1 0 0 1 1 1V20a1 1 0 0 1-1 1A17 17 0 0 1 3 4a1 1 0 0 1 1-1h3.5a1 1 0 0 1 1 1c0 1.25.2 2.45.6 3.6a1 1 0 0 1-.25 1z" fill="#fff"/></svg>0381 - 72946183</p>
      <p class="line"><svg width="8" height="6" viewBox="0 0 16 12"><rect width="16" height="12" rx="1" fill="#fff"/><path d="M0 0 8 7 16 0" fill="none" stroke="var(--navy)" stroke-width="1.5"/></svg>Mail@sonnenweg-touren .de</p>
    </div>
    <div class="badge badge--cta"><span>Jetzt</span><span>informieren</span><span>&amp; Platz</span><span>sichern!</span></div>
    <p class="url">www.sonnenweg-touren.de</p>
  </section>

</div>
</body>
</html>
```